Shopify Theme design for a Subscription Cyber security service for consumers and SMB

Looking for the Theme design for our shopify store that will be selling a Cyber Security subscription service to Consumers and SMB. The service provides enterprise grade tools at consumer prices.
we have logos and colour scheme ready to go, however we don't use 2, 4, 7 or 8 typically in what we do.
it will be a pretty simple shop and it will be using the subscriptions app from shopify also.
We will need all the standard pages such as:
the home page
pages
Product/Subscription page
Cart
404
And any others that are standard in a theme that I have not listed
Cyber Security
4 page

```html
<!DOCTYPE html>
<html lang="en">
<head>
<meta charset="utf-8">
<title>Cyberlume – Cyber Security Subscription</title>
<link href="https://fonts.googleapis.com/css2?family=Montserrat:wght@400;500;600;700;800&display=swap" rel="stylesheet">
<style>
:root{
  --purple:#5522d9;
  --purple-dark:#4318b8;
  --ink:#111118;
  --text:#444450;
  --muted:#6a6a78;
  --lav:#efeafc;
  --navy:#0b1a3d;
  --footer:#0a0c24;
  --white:#ffffff;
}
*{box-sizing:border-box;margin:0;padding:0}
html,body{width:1200px;height:3987px;overflow:hidden}
body{font-family:'Montserrat',sans-serif;color:var(--ink);background:var(--white);position:relative}
.abs{position:absolute}
.accent{color:var(--purple)}

/* header */
.hero{left:0;top:0;width:1200px;height:646px;background:linear-gradient(160deg,#f3f0fb 0%,#ffffff 45%,#efe8ff 100%)}
.brand{display:flex;align-items:center;gap:12px;font-size:25px;font-weight:500;letter-spacing:2px;color:#2a2f66}
.brand-box{width:34px;height:34px;border:3px solid #3b5bdb;border-radius:6px}
.nav{top:34px;left:485px;display:flex;gap:44px;font-size:14px;font-weight:500;color:#333}
.cart{left:1054px;top:30px}
.welcome{left:108px;top:210px;font-size:30px;font-weight:600}
.hero-title{left:108px;top:252px;font-size:58px;font-weight:700;color:var(--purple)}
.hero-text{left:108px;top:336px;width:470px;font-size:14.5px;line-height:34px;color:#222}
.btn{display:flex;align-items:center;justify-content:center;background:var(--purple);color:#fff;font-weight:700;border-radius:30px;font-size:15px}
.btn-hero{left:108px;top:425px;width:168px;height:46px}
.hero-photo{left:582px;top:135px;width:514px;height:441px;background:linear-gradient(135deg,#b89a7a 0%,#6e5a4c 45%,#e8dccd 100%);border-radius:2px}
.hero-bar-r{left:1096px;top:152px;width:20px;height:430px;background:var(--purple)}
.hero-bar-b{left:604px;top:576px;width:330px;height:12px;background:var(--purple)}
.float-card{background:#fff;border-bottom:4px solid var(--purple);box-shadow:0 6px 18px rgba(60,30,140,.15);border-radius:4px;display:flex;gap:8px;padding:10px}
.float-card h4{color:var(--purple);font-size:17px;font-weight:600;white-space:nowrap}
.float-card p{font-size:10.5px;line-height:16px;color:#555;margin-top:3px}
.fc-icon{width:28px;height:28px;border-radius:7px;background:#4c7bf0;flex:none;margin-top:2px}
.fc1{left:534px;top:142px;width:212px}
.fc2{left:924px;top:514px;width:212px}
.lock-badge{left:884px;top:422px;width:62px;height:62px;border-radius:50%;background:#4a2bd8;border:4px solid #8a73ff}

h2.section{position:absolute;left:0;width:1200px;text-align:center;font-size:37px;font-weight:700}

/* steps */
.step{width:280px}
.step svg{display:block}
.step h3{font-size:21px;font-weight:700;line-height:34px;margin-top:40px}
.step p{font-size:14px;line-height:32px;color:var(--text);margin-top:8px}

/* content cards */
.card{width:314px;height:452px;background:#fff;box-shadow:0 2px 14px rgba(0,0,0,.12);border-radius:4px}
.card-img{position:absolute;left:7px;top:6px;width:300px;height:198px;border-radius:3px}
.card h3{position:absolute;left:20px;top:228px;font-size:21px;font-weight:700}
.card p{position:absolute;left:18px;top:270px;width:285px;font-size:14px;line-height:32px;color:var(--text)}
.card .btn{position:absolute;left:20px;top:385px;width:262px;height:45px}
.arrow{width:44px;height:44px;border-radius:50%;display:flex;align-items:center;justify-content:center}

/* subscribe */
.sub-band{left:0;top:1803px;width:1200px;height:428px;background:linear-gradient(100deg,#0a1f4d 0%,#0e2f6b 55%,#0a1a45 100%)}
.sub-art{left:600px;top:1803px;width:600px;height:428px;background:radial-gradient(ellipse at 50% 55%,rgba(60,150,230,.75) 0%,rgba(20,70,150,.35) 40%,rgba(10,30,77,0) 70%)}
.sub-title{left:112px;top:1892px;font-size:40px;font-weight:700;color:#fff}
.sub-text{left:108px;top:1956px;width:580px;font-size:15.5px;line-height:38px;color:#fff}
.btn-white{left:108px;top:2094px;width:168px;height:46px;background:#fff;color:var(--purple);border-radius:30px;display:flex;align-items:center;justify-content:center;font-weight:700;font-size:15px}

/* pricing */
.pricing-bg{left:0;top:2231px;width:1200px;height:718px;background:linear-gradient(180deg,#f2f4fa 0%,#ffffff 40%,#eef0f7 100%)}
.plan{background:#fff;box-shadow:0 4px 18px rgba(0,0,0,.08);text-align:center}
.plan-head{height:165px;background:#f1f7fb;padding-top:38px}
.plan-name{font-size:18px;color:var(--purple);font-weight:500}
.price{font-size:44px;font-weight:800;color:var(--purple-dark);margin-top:8px}
.price sup{font-size:24px;vertical-align:18px;margin-right:6px}
.per{font-size:11px;font-weight:700;color:var(--purple)}
.plan-body{font-size:14px;line-height:26px;color:#222;padding:30px 10px 0}
.plan .pbtn{margin:24px auto 0;width:124px;height:34px;border:2px solid var(--purple);border-radius:20px;font-size:10px;font-weight:700;color:var(--purple);display:flex;align-items:center;justify-content:center}
.plan-bar{position:absolute;left:0;bottom:-4px;width:100%;height:6px;background:var(--purple)}
.premium .plan-name,.premium .price,.premium .per{color:#fff}
.premium .pbtn{background:var(--purple);color:#fff}

/* faq */
.faq{left:183px;width:828px;background:#fff;box-shadow:0 2px 10px rgba(0,0,0,.12);border-radius:3px;padding:0 16px}
.faq-q{height:53px;display:flex;align-items:center;justify-content:space-between;font-size:15px;font-weight:600}
.faq-q span.sign{font-size:28px;font-weight:500}
.faq-a{font-size:13px;line-height:26px;color:var(--muted);padding-right:40px;margin-top:-6px}

/* footer */
.footer{left:0;top:3570px;width:1200px;height:417px;background:var(--footer)}
.foot-brand{left:108px;top:3685px;color:#fff;display:flex;align-items:center;gap:12px;font-size:22px;letter-spacing:2px;font-weight:500}
.foot-brand .brand-box{border-color:#5b7bff}
.social{top:3801px;width:32px;height:32px;border-radius:50%;background:#fff}
.foot-h{font-size:21px;font-weight:600;color:#fff}
.foot-list{list-style:none;font-size:14px;line-height:28px;color:#fff}
.contact-row{display:flex;align-items:center;gap:8px;height:28px;font-size:14px;color:#fff}
.sub-box{left:887px;top:3659px;width:198px;height:239px;background:var(--purple);border-radius:6px;text-align:center;color:#fff}
.sub-box h4{font-size:22px;font-weight:600;margin-top:36px}
.sub-box p{font-size:12.5px;line-height:28px;margin-top:6px}
.email{margin:18px auto 0;width:164px;height:36px;border:1px solid #fff;border-radius:20px;display:flex;align-items:center;justify-content:space-between;padding:0 3px 0 9px;font-size:10px}
.email i{width:30px;height:30px;border-radius:50%;background:#fff;display:flex;align-items:center;justify-content:center}
.foot-line{left:108px;top:3932px;width:976px;height:1px;background:#fff;opacity:.6}
.copy{left:0;top:3946px;width:1200px;text-align:center;font-size:14px;color:#fff}
</style>
</head>
<body>

<!-- Hero -->
<div class="abs hero"></div>
<div class="abs brand" style="left:108px;top:30px"><span class="brand-box"></span>CYBERLUME</div>
<nav class="abs nav"><span>HOME</span><span>ABOUT US</span><span>OUR PRODUCT</span><span>SHOP</span><span>CONTACT US</span></nav>
<svg class="abs cart" width="30" height="28" viewBox="0 0 30 28" fill="none" stroke="#222" stroke-width="2"><path d="M1 3h5l4 15h15l3-11H8"/><circle cx="12" cy="24" r="2"/><circle cx="23" cy="24" r="2"/></svg>

<div class="abs welcome">WELCOME TO</div>
<div class="abs hero-title">CYBERLUME</div>
<p class="abs hero-text">Lorem Ipsum is simply dummy text of the printing and typesetting industry. Lorem Ipsum has been the industry's</p>
<div class="abs btn btn-hero">GET STARTED</div>

<div class="abs hero-bar-r"></div>
<div class="abs hero-bar-b"></div>
<div class="abs hero-photo" role="img" aria-label="Photo of a family using a laptop together at home"></div>
<div class="abs lock-badge"></div>
<div class="abs float-card fc1"><span class="fc-icon"></span><div><h4>Testing</h4><p>Lorem Ipsum is simply dummy text of the printing</p></div></div>
<div class="abs float-card fc2"><span class="fc-icon" style="background:#4a2bd8"></span><div><h4>Cyber Security</h4><p>Lorem Ipsum is simply dummy text of the printing</p></div></div>

<!-- Subscription steps -->
<h2 class="section" style="top:756px">CYBER SECURITY <span class="accent">SUBSCRIPTION</span></h2>

<div class="abs step" style="left:128px;top:867px">
<svg width="62" height="62" viewBox="0 0 62 62" fill="none" stroke="#5522d9" stroke-width="2.5"><rect x="3" y="4" width="56" height="52" rx="4"/><line x1="3" y1="16" x2="59" y2="16"/><circle cx="10" cy="10" r="1.5"/><circle cx="16" cy="10" r="1.5"/><circle cx="16" cy="32" r="5"/><circle cx="31" cy="32" r="5"/><circle cx="46" cy="32" r="5"/><line x1="12" y1="46" x2="50" y2="46"/></svg>
<h3>Submit your Request</h3>
<p>Lorem Ipsum is simply dummy text of the printing and typesetting industry. Lorem Ipsum has been the</p>
</div>
<div class="abs step" style="left:466px;top:862px">
<svg width="62" height="68" viewBox="0 0 62 68" fill="none" stroke="#5522d9" stroke-width="2.5"><rect x="4" y="16" width="54" height="36" rx="3"/><line x1="31" y1="52" x2="31" y2="62"/><line x1="18" y1="63" x2="44" y2="63"/><circle cx="31" cy="22" r="14" fill="#fff"/><circle cx="31" cy="22" r="7"/></svg>
<h3 style="margin-top:34px">Wait for delivery</h3>
<p>Lorem Ipsum is simply dummy text of the printing and typesetting industry. Lorem Ipsum has been the</p>
</div>
<div class="abs step" style="left:796px;top:867px">
<svg width="64" height="64" viewBox="0 0 64 64" fill="none" stroke="#5522d9" stroke-width="2.5"><circle cx="32" cy="14" r="10"/><path d="M14 42c2-10 10-16 18-16s16 6 18 16"/><path d="M12 46l3 6 6 1-4 4 1 6-6-3-6 3 1-6-4-4 6-1z" fill="#5522d9"/><path d="M32 46l3 6 6 1-4 4 1 6-6-3-6 3 1-6-4-4 6-1z" fill="#5522d9"/><path d="M52 46l3 6 6 1-4 4 1 6-6-3-6 3 1-6-4-4 6-1z" fill="#5522d9"/></svg>
<h3 style="width:230px">Revise until you're happy</h3>
<p style="margin-top:0">Lorem Ipsum is simply dummy text of the printing and typesetting</p>
</div>

<!-- Content examples -->
<h2 class="section" style="top:1168px">CONTENT <span class="accent">EXAMPLES</span></h2>
<div class="abs arrow" style="left:28px;top:1456px;background:#555"><svg width="16" height="16" viewBox="0 0 16 16" fill="none" stroke="#fff" stroke-width="2.5"><path d="M10 2L4 8l6 6"/></svg></div>
<div class="abs arrow" style="left:1124px;top:1456px;background:var(--purple)"><svg width="16" height="16" viewBox="0 0 16 16" fill="none" stroke="#fff" stroke-width="2.5"><path d="M6 2l6 6-6 6"/></svg></div>

<div class="abs card" style="left:108px;top:1251px">
<div class="card-img" role="img" aria-label="Photo of hands typing on a keyboard with a digital security shield" style="background:linear-gradient(135deg,#0a2748,#1d5e9a 60%,#0a1c38)"></div>
<h3>Lorem Ipsum is simply</h3>
<p>Lorem Ipsum is simply dummy text of the printing and typesetting industry. Lorem Ipsum has been the</p>
<div class="btn">READ MORE</div>
</div>
<div class="abs card" style="left:443px;top:1251px">
<div class="card-img" role="img" aria-label="Photo of a hand touching a cyber security login interface" style="background:linear-gradient(135deg,#3d79b8,#7fb2e0 55%,#25507f)"></div>
<h3>Lorem Ipsum is simply</h3>
<p>Lorem Ipsum is simply dummy text of the printing and typesetting industry. Lorem Ipsum has been the</p>
<div class="btn">READ MORE</div>
</div>
<div class="abs card" style="left:771px;top:1251px">
<div class="card-img" role="img" aria-label="Photo of a laptop keyboard with a glowing padlock overlay" style="background:linear-gradient(135deg,#22253a,#3c4364 55%,#5a3c32)"></div>
<h3>Lorem Ipsum is simply</h3>
<p>Lorem Ipsum is simply dummy text of the printing and typesetting industry. Lorem Ipsum has been the</p>
<div class="btn">READ MORE</div>
</div>

<!-- Subscribe -->
<div class="abs sub-band"></div>
<div class="abs sub-art" role="img" aria-label="Illustration of a glowing digital security shield with a keyhole"></div>
<div class="abs sub-title">SUBSCRIBE NOW..</div>
<p class="abs sub-text">Lorem Ipsum is simply dummy text of the printing and typesetting industry. Lorem Ipsum has been the industry's standard dummy text ever since the 1500s</p>
<div class="abs btn-white">SUBSCRIBE</div>

<!-- Pricing -->
<div class="abs pricing-bg"></div>
<h2 class="section" style="top:2318px">SIMPLE AND <span class="accent">FLEXIBLE PRICING</span></h2>

<div class="abs plan" style="left:260px;top:2430px;width:217px;height:397px">
<div class="plan-head"><div class="plan-name">Basic</div><div class="price"><sup>$</sup>19.10</div><div class="per">Per Month</div></div>
<div class="plan-body">Lorem ipsum dolor sit amet, consectetur adipiscing elit, sed do eiusmod tempor incididunt ut labore et</div>
<div class="pbtn">GET STARTED</div>
<div class="plan-bar"></div>
</div>
<div class="abs plan" style="left:717px;top:2430px;width:218px;height:397px">
<div class="plan-head" style="background:#f3effd"><div class="plan-name">Extreme inspection</div><div class="price"><sup>$</sup>79.90</div><div class="per">Per Month</div></div>
<div class="plan-body">Lorem ipsum dolor sit amet, consectetur adipiscing elit, sed do eiusmod tempor incididunt ut labore et</div>
<div class="pbtn" style="margin-top:14px">GET STARTED</div>
<div class="plan-bar"></div>
</div>
<div class="abs plan premium" style="left:477px;top:2412px;width:240px;height:433px;box-shadow:0 6px 24px rgba(0,0,0,.14)">
<svg class="abs" style="left:0;top:0" width="240" height="184" viewBox="0 0 240 184"><path d="M0 0h240v160l-120 24L0 160z" fill="#5522d9"/></svg>
<div style="position:relative;padding-top:34px"><div class="plan-name">Premium</div><div class="price" style="margin-top:4px"><sup>$</sup>39.30</div><div class="per">Per Month</div></div>
<div class="plan-body" style="padding-top:82px">Lorem ipsum dolor sit amet, consectetur adipiscing elit, sed do eiusmod tempor incididunt ut labore et</div>
<div class="pbtn" style="margin-top:26px">GET STARTED</div>
</div>

<!-- FAQ -->
<h2 class="section" style="top:3024px">FREQUENTLY <span class="accent">ASKED QUESTION</span></h2>
<div class="abs faq" style="top:3100px"><div class="faq-q">Lorem Ipsum is simply dummy text of the printing and typesetting industry<span class="sign">+</span></div></div>
<div class="abs faq" style="top:3161px"><div class="faq-q">Lorem Ipsum is simply dummy text of the printing and typesetting industry<span class="sign">+</span></div></div>
<div class="abs faq" style="top:3221px"><div class="faq-q">Lorem Ipsum is simply dummy text of the printing and typesetting industry<span class="sign">+</span></div></div>
<div class="abs faq" style="top:3281px;height:128px"><div class="faq-q">Lorem Ipsum is simply dummy text of the printing and typesetting industry<span class="sign">&minus;</span></div>
<p class="faq-a">Lorem Ipsum is simply dummy text of the printing and typesetting industry. Lorem Ipsum has been the industry's standard dummy text ever since the 1500s, when an unknown printer took a galley of type and scrambled it to make a type specimen book.</p></div>
<div class="abs faq" style="top:3418px"><div class="faq-q">Lorem Ipsum is simply dummy text of the printing and typesetting industry<span class="sign">+</span></div></div>

<!-- Footer -->
<div class="abs footer"></div>
<div class="abs foot-brand"><span class="brand-box"></span>CYBERLUME</div>
<span class="abs social" style="left:123px"></span>
<span class="abs social" style="left:167px"></span>
<span class="abs social" style="left:210px"></span>

<div class="abs foot-h" style="left:407px;top:3659px">Page Links</div>
<ul class="abs foot-list" style="left:410px;top:3713px"><li>Home</li><li>About Us</li><li>Our Product</li><li>Shop</li><li>Contact Us</li></ul>

<div class="abs foot-h" style="left:632px;top:3659px">Contact Details</div>
<div class="abs" style="left:630px;top:3715px">
<div class="contact-row"><svg width="12" height="14" viewBox="0 0 12 14" fill="#fff"><path d="M2 1l3 0 1 3-2 1c1 2 2 3 4 4l1-2 3 1v3c-6 1-11-4-10-10z"/></svg>+1 555 010 2040</div>
<div class="contact-row"><svg width="14" height="10" viewBox="0 0 14 10" fill="none" stroke="#fff" stroke-width="1.5"><rect x="1" y="1" width="12" height="8"/><path d="M1 1l6 5 6-5"/></svg>info@cyberlume.example</div>
<div class="contact-row"><svg width="12" height="14" viewBox="0 0 12 14" fill="#fff"><path d="M6 0a5 5 0 0 1 5 5c0 4-5 9-5 9S1 9 1 5a5 5 0 0 1 5-5zm0 3a2 2 0 1 0 0 4 2 2 0 0 0 0-4z"/></svg>lorem ipsum lorem</div>
<div class="contact-row" style="padding-left:20px">ipsum lorem ipsum</div>
</div>

<div class="abs sub-box">
<h4>Subscribe</h4>
<p>Are you interested in<br>following us for Getting<br>Business Update</p>
<div class="email">Your Email Address<i><svg width="16" height="12" viewBox="0 0 16 12" fill="none" stroke="#5522d9" stroke-width="2"><path d="M1 6h13M9 1l5 5-5 5"/></svg></i></div>
</div>

<div class="abs foot-line"></div>
<div class="abs copy">Copyright © 2024 Cyberlume | All Rights Reserved</div>

</body>
</html>
```